Flyer for the Radiant Harvest Worship Day 2020

I am looking to create a flyer for a one day prayer retreat our church is organizing.
This flyer will be posted on social media, websites and will also be printed so it can be mailed to people.
I am looking for something professional, with good use of our logo and band colors (logo colors).
I am counting on the designer's skill, creativity, art and knowledge of media communication to produce a flyer that will effectively and quickly convey the message we are trying to spread.
CONTENT OF THE FLYER:
Event title: Radiant Harvest Worship Day
Date: Tuesday July 2nd, 2020
Time: 11:00AM - 7:00PM
Belmora Hotel, 4876 Willowmere Street, Portland, Maine 04987 (Room: Evergrove)
Event Key words to highlight what the event is about: Prayer, Sharing the Word, Panel discussion, prophecy, Impartation.
Key phrases:
A one day prayer retreat.
Jesus Chris is Lord
Contact info:
www.toluvek.org
Phone: 207 555 0183
Email: contact@brightmeadowfold.org

```html
<!DOCTYPE html>
<html lang="en">
<head>
<meta charset="utf-8">
<title>Radiant Harvest Worship Day 2020</title>
<link rel="stylesheet" href="https://fonts.googleapis.com/css2?family=Montserrat:wght@400;500;600;700;800&family=Yellowtail&family=Kaushan+Script&display=swap">
<style>
  :root {
    --page: #ffffff;
    --orange: #f0901e;
    --orange-deep: #c47318;
    --brown: #2a1f17;
    --night: #050608;
    --navy-deep: #1f2f52;
    --ink: #14294a;
    --white: #ffffff;
  }
  * { margin: 0; padding: 0; box-sizing: border-box; }
  html, body {
    width: 1200px; height: 817px; overflow: hidden;
    background: var(--page);
    font-family: "Montserrat", sans-serif;
  }
  .flyer {
    position: absolute; left: 312px; top: 34px;
    width: 582px; height: 753px; overflow: hidden;
  }
  .flyer-backdrop { position: absolute; inset: 0; }
  .brand {
    position: absolute; left: 50px; top: 96px;
    display: flex; align-items: center; gap: 8px;
  }
  .brand-dot { width: 12px; height: 12px; border-radius: 50%; background: var(--orange); }
  .brand-name {
    font-family: "Montserrat", sans-serif;
    font-weight: 500; font-size: 30px; letter-spacing: 1px;
    color: var(--white); line-height: 1;
  }
  .title-kicker {
    position: absolute; left: 150px; top: 348px;
    font-family: "Kaushan Script", cursive; font-size: 26px;
    color: var(--white); white-space: nowrap; line-height: 1.2;
  }
  .title-main {
    position: absolute; left: 34px; top: 378px;
    font-family: "Yellowtail", cursive; font-size: 80px; line-height: 1;
    color: var(--white); white-space: nowrap;
  }
  .retreat-label {
    position: absolute; left: 25px; top: 480px;
    font-size: 12.5px; letter-spacing: 3px; font-weight: 500; color: var(--ink);
  }
  .retreat-phrase {
    position: absolute; left: 24px; top: 494px;
    font-size: 26px; letter-spacing: 3px; font-weight: 500; color: var(--ink);
    line-height: 1;
  }
  .rule {
    position: absolute; left: 25px; top: 526px;
    width: 373px; height: 2px; background: var(--ink);
  }
  .when {
    position: absolute; left: 25px; top: 544px; color: var(--white);
    font-weight: 800; line-height: 1.3;
  }
  .when-day { font-size: 21px; letter-spacing: 0.5px; line-height: 1.1; }
  .when-date, .when-time { font-size: 12px; }
  .divider {
    position: absolute; left: 147px; top: 545px;
    width: 2px; height: 59px; background: var(--white);
  }
  .where {
    position: absolute; left: 158px; top: 547px;
    font-size: 15px; font-weight: 600; line-height: 1.08; color: var(--white);
  }
  .highlights {
    position: absolute; left: 25px; top: 618px;
    font-size: 14.5px; font-weight: 500; color: var(--ink);
    line-height: 23px; letter-spacing: 0.3px;
  }
  .highlights span::before { content: "\2022\00a0"; }
  .highlights span { margin-right: 6px; }
  .contact-bar {
    position: absolute; left: 0; top: 685px; width: 582px; height: 47px;
    display: flex; align-items: center; gap: 6px; padding-left: 25px;
    color: var(--ink); font-weight: 700; font-size: 12.5px;
  }
  .contact-item { display: flex; align-items: center; gap: 6px; margin-right: 4px; }
  .contact-icon { flex: none; }
</style>
</head>
<body>
<div class="flyer">
  <svg class="flyer-backdrop" width="582" height="753" viewBox="0 0 582 753">
    <defs>
      <linearGradient id="warm" x1="0" y1="0" x2="0.25" y2="1">
        <stop offset="0" stop-color="var(--brown)"/>
        <stop offset="0.45" stop-color="var(--orange-deep)"/>
        <stop offset="1" stop-color="var(--orange)"/>
      </linearGradient>
      <linearGradient id="night" x1="0" y1="0" x2="0" y2="1">
        <stop offset="0" stop-color="var(--night)"/>
        <stop offset="0.55" stop-color="#0c1220"/>
        <stop offset="1" stop-color="var(--navy-deep)"/>
      </linearGradient>
      <radialGradient id="spot" cx="0.5" cy="0.5" r="0.5">
        <stop offset="0" stop-color="#ffffff"/>
        <stop offset="0.45" stop-color="#d0d0d0"/>
        <stop offset="0.8" stop-color="#2a2a2a" stop-opacity="0.6"/>
        <stop offset="1" stop-color="#000000" stop-opacity="0"/>
      </radialGradient>
    </defs>
    <rect width="582" height="753" fill="url(#warm)"/>
    <polygon points="36,0 582,0 582,753 580,753" fill="url(#night)"/>
    <ellipse cx="400" cy="210" rx="190" ry="210" fill="url(#spot)" role="img" aria-label="Photograph of a young man praying with clasped hands under a spotlight"/>
    <polygon points="0,685 546,685 581,732 0,732" fill="var(--white)"/>
  </svg>

  <div class="brand">
    <span class="brand-dot"></span>
    <span class="brand-name">TOLUVEK</span>
  </div>

  <div class="title-kicker">Radiant Harvest</div>
  <div class="title-main">Worship Day</div>

  <div class="retreat-label">A ONE DAY PRAYER RETREAT</div>
  <div class="retreat-phrase">Jesus Chris is Lord</div>
  <div class="rule"></div>

  <div class="when">
    <div class="when-day">TUESDAY</div>
    <div class="when-date">JULY 2ND, 2020</div>
    <div class="when-time">11:00AM - 7:00PM</div>
  </div>
  <div class="divider"></div>
  <div class="where">
    Belmora Hotel,<br>
    4876 Willowmere Street, Portland,<br>
    Maine 04987 (Room: Evergrove)
  </div>

  <div class="highlights">
    <span>PRAYER</span><span>SHARING THE WORD</span><span>PANEL DISCUSSION</span><br>
    <span>PROPHECY</span><span>IMPARTATION</span>
  </div>

  <div class="contact-bar">
    <div class="contact-item">
      <svg class="contact-icon" width="28" height="28" viewBox="0 0 28 28" fill="none" stroke="var(--ink)" stroke-width="1.6">
        <circle cx="14" cy="14" r="13"/>
        <path d="M9.5 7.5l3 3-1.6 2c.9 1.8 2.3 3.2 4.1 4.1l2-1.6 3 3-2 2c-5.5-.4-10-4.9-10.5-10.5z" fill="var(--ink)" stroke="none"/>
      </svg>
      <span>207 555 0183</span>
    </div>
    <div class="contact-item">
      <svg class="contact-icon" width="30" height="22" viewBox="0 0 30 22" fill="none" stroke="var(--ink)" stroke-width="1.6">
        <rect x="1" y="1" width="28" height="20"/>
        <path d="M1 1l14 11 14-11M1 21l10-9M29 21l-10-9"/>
      </svg>
      <span>contact@brightmeadowfold.org</span>
    </div>
    <div class="contact-item">
      <svg class="contact-icon" width="28" height="28" viewBox="0 0 28 28" fill="none" stroke="var(--ink)" stroke-width="1.5">
        <circle cx="14" cy="14" r="12.5"/>
        <ellipse cx="14" cy="14" rx="5.5" ry="12.5"/>
        <path d="M14 1.5v25M1.5 14h25M3.5 7.5h21M3.5 20.5h21"/>
      </svg>
      <span>www.toluvek.org</span>
    </div>
  </div>
</div>
</body>
</html>
```